RTV Photography Business Card Design

I would like a business card designed in the shape of a camera.
Would like to see various camera designs. Would like to see what the card looks like in different colors. Would like to see which logo looks better on the various camera designs so please show me some with the white logo and some with the black logo. If you need a different file formats please let me know.
Project Deadline Extended Reason: My grandfather passed away and dealing with funeral plans so need to extend deadline. Added Tuesday, March 1, 2016
Project Deadline Extended
Reason: I just got back from out of town. My grandfather's passing was the primary focus for me these past few weeks and the funeral is over so now I will concentrate on picking my business card design. I really appreciate each designer who has taken the time to submit a design. Your effort has not gone unnoticed. I look forward to seeing more amazing designs.
Industry/Entity Type
Business
Contact Information for Business Card
Wren
757-418-2096
https://www.facebook.com/rtvphotographyfreelance/
DoraWren@rtv-photography.example
Look and feel

```html
<!DOCTYPE html>
<html lang="en">
<head>
<meta charset="utf-8">
<title>RTV Photography Business Card</title>
<link href="https://fonts.googleapis.com/css2?family=Cinzel:wght@400&family=Open+Sans:wght@400;700&display=swap" rel="stylesheet">
<style>
  :root {
    --backdrop: #ecebe8;
    --gold-deep: #b8621c;
    --gold-mid: #e0a23c;
    --gold-light: #fbe3a0;
    --gold-text: #c9902e;
    --name-orange: #d88a1c;
    --ink: #333333;
    --paper: #ffffff;
    --ghost: #f1f1f1;
  }
  html, body {
    margin: 0;
    width: 1200px;
    height: 900px;
    overflow: hidden;
    background: var(--backdrop);
  }
  .canvas {
    position: relative;
    width: 1200px;
    height: 900px;
  }
  .camera {
    position: absolute;
    width: 600px;
    height: 383px;
    filter: drop-shadow(0 10px 16px rgba(0,0,0,0.18));
  }
  .camera-front { left: 70px; top: 50px; }
  .camera-back { left: 530px; top: 460px; }
  .card {
    position: absolute;
    inset: 0;
    overflow: hidden;
    clip-path: path("M0 40 H70 V26 H130 V40 H190 L215 0 H385 L410 40 H600 V383 H0 Z");
  }
  .card-front {
    background: linear-gradient(115deg, var(--gold-deep) 0%, var(--gold-mid) 30%, var(--gold-light) 48%, var(--gold-mid) 68%, var(--gold-deep) 100%);
  }
  .card-back { background: var(--paper); }
  .brand {
    position: absolute;
    display: flex;
    flex-direction: column;
    align-items: center;
  }
  .brand-dot { border-radius: 50%; }
  .brand-name {
    font-family: "Cinzel", serif;
    letter-spacing: 1px;
    white-space: nowrap;
  }
  .card-front .brand { left: 0; right: 0; top: 112px; }
  .card-front .brand-dot {
    width: 104px; height: 104px;
    background: var(--paper);
  }
  .card-front .brand-name {
    margin-top: 24px;
    font-size: 34px;
    color: var(--paper);
  }
  .ghost-circle {
    position: absolute;
    left: 20px; top: 0;
    width: 400px; height: 400px;
    border-radius: 50%;
    background: var(--ghost);
  }
  .card-back .brand { left: 20px; top: 110px; width: 300px; }
  .card-back .brand-dot {
    width: 88px; height: 88px;
    background: linear-gradient(135deg, var(--gold-light), var(--gold-mid) 55%, var(--gold-deep));
  }
  .card-back .brand-name {
    margin-top: 18px;
    font-size: 24px;
    color: var(--gold-text);
  }
  .contact {
    position: absolute;
    left: 338px; top: 110px;
    font-family: "Open Sans", sans-serif;
    color: var(--ink);
  }
  .person-name {
    margin: 0;
    font-size: 19px;
    font-weight: 700;
    color: var(--name-orange);
  }
  .person-role {
    margin: 0 0 16px;
    font-size: 13px;
  }
  .contact-list {
    list-style: none;
    margin: 0; padding: 0;
    font-size: 12.5px;
    line-height: 24px;
  }
  .contact-list li {
    display: flex;
    align-items: center;
    gap: 7px;
    white-space: nowrap;
  }
  .contact-list svg {
    width: 11px; height: 11px;
    fill: var(--name-orange);
    flex: none;
  }
</style>
</head>
<body>
<main class="canvas">
  <div class="camera camera-front">
    <section class="card card-front" aria-label="Card front">
      <div class="brand">
        <span class="brand-dot"></span>
        <span class="brand-name">RTV PHOTOGRAPHY</span>
      </div>
    </section>
  </div>

  <div class="camera camera-back">
    <section class="card card-back" aria-label="Card back">
      <span class="ghost-circle"></span>
      <div class="brand">
        <span class="brand-dot"></span>
        <span class="brand-name">RTV PHOTOGRAPHY</span>
      </div>
      <div class="contact">
        <p class="person-name">Wren</p>
        <p class="person-role">Photographer</p>
        <ul class="contact-list">
          <li><svg viewBox="0 0 12 12"><path d="M2.5 0.5l2 2-1 1.5c.8 1.6 2 2.8 3.5 3.5l1.5-1 2 2-1.2 1.8C5.5 10 2 6.5 1 2z"/></svg>757-418-2096</li>
          <li><svg viewBox="0 0 12 12"><circle cx="6" cy="6" r="5.5"/></svg>facebook.com/rtvphotographyfreelance</li>
          <li><svg viewBox="0 0 12 12"><rect x="0.5" y="2" width="11" height="8" rx="1"/></svg>DoraWren@rtv-photography.example</li>
          <li><svg viewBox="0 0 12 12"><path d="M4 8l4-4" stroke="#d88a1c" stroke-width="1.6"/><rect x="0.8" y="6" width="5" height="3.4" rx="1.7" transform="rotate(-45 3.3 7.7)" fill="none" stroke="#d88a1c" stroke-width="1.4"/><rect x="6.2" y="2.6" width="5" height="3.4" rx="1.7" transform="rotate(-45 8.7 4.3)" fill="none" stroke="#d88a1c" stroke-width="1.4"/></svg>www.rtv-photography.example</li>
        </ul>
      </div>
    </section>
  </div>
</main>
</body>
</html>
```